I am looking for help designing my new business cards. I would like rounded edges and a raised logo on the back of the card. I have 2 Logos. One with a boat in it and one without. I'd like the one on the back to be the one that includes the boat and just the name on the front. I have included multiple formats of my logo. Please let me know if you need anymore.

Target Market(s)

Potential buyers and other sales brokers

Industry/Entity Type

Sales - Yacht / Boat Sales

Contact Information for Business Card

Id liike the front to include just the business name portion of the logo along with my name (Corwin Dalby), phone number (555.318.6027), website address (www.dalbymarineco.example) and not my physical address but just "Wrenport, GA". The back should include my full logo that has the boat included. This portion I'd prefer raised amd take up the majority of the space there. Thanks!!

Colors
0054AA
0677BA
7BADD7
CADEEF
E8F1F8
0094D4
00A9DD
6FCCEA
C7EBF8
E9F6FB

Requirements
Must have
• Double sided
Nice to have
• My email address: Corwin@dalbymarineco.example The NMTG logo somewhere small on the front of the card
Should not have
• My full address, prefer only "Wrenport, GA"

```html
<!DOCTYPE html>
<html lang="en">
<head>
<meta charset="utf-8">
<title>Dalby Marine Co. — Business Card</title>
<link href="https://fonts.googleapis.com/css2?family=Lato:wght@400;700;900&display=swap" rel="stylesheet">
<style>
  :root {
    --backdrop: #9a9a9a;
    --paper: #f7f7f5;
    --navy: #1f3f7a;
    --navy-deep: #0c2566;
    --sky: #2b8fcb;
    --ink-grey: #4a4a4a;
    --edge: #2b8fcb;
  }
  * { box-sizing: border-box; margin: 0; padding: 0; }
  html, body {
    width: 1200px; height: 976px; overflow: hidden;
    background: var(--backdrop);
    font-family: "Lato", sans-serif;
  }
  .sheet {
    width: 1200px; height: 976px;
    display: flex; flex-direction: column; align-items: center;
    justify-content: space-evenly;
  }
  .card {
    position: relative;
    width: 760px; height: 434px;
    border-radius: 34px;
    box-shadow: 0 3px 0 var(--edge), 0 14px 28px rgba(0,0,0,.28);
    overflow: hidden;
  }
  /* Front */
  .card-front { background: var(--paper); }
  .holder-name {
    position: absolute; left: 60px; top: 46px;
    font-weight: 900; font-size: 42px; letter-spacing: .5px;
    color: var(--navy); text-transform: uppercase;
  }
  .holder-email {
    position: absolute; left: 60px; top: 98px;
    font-size: 21px; color: var(--sky);
  }
  .boat-art {
    position: absolute; left: 40px; top: 180px;
    width: 400px; height: 220px;
    border-radius: 120px 40px 140px 60px;
    background: linear-gradient(160deg, #e4edf7 0%, #b9d6ee 55%, #6fb3e0 100%);
  }
  .contact {
    position: absolute; right: 48px; top: 160px;
    text-align: right; line-height: 1.4;
  }
  .contact-row {
    display: flex; justify-content: flex-end; align-items: center; gap: 12px;
    font-size: 22px; color: var(--ink-grey);
  }
  .contact-row.company {
    font-weight: 900; font-size: 24px; color: var(--sky);
  }
  .contact-row svg { width: 18px; height: 18px; flex: none; }
  .icon-slot { width: 18px; flex: none; }
  /* Back */
  .card-back { background: var(--navy-deep); display: flex; align-items: center; justify-content: center; }
  .brand-name {
    font-weight: 900; font-size: 66px; letter-spacing: 2px;
    color: #ffffff; text-transform: uppercase;
  }
</style>
</head>
<body>
<main class="sheet">
  <section class="card card-front" aria-label="Card front">
    <h1 class="holder-name">Corwin Dalby</h1>
    <p class="holder-email">corwin@dalbymarineco.example</p>
    <div class="boat-art" role="img" aria-label="Line illustration of a center-console fishing boat cutting through waves"></div>
    <div class="contact">
      <div class="contact-row company">Dalby Marine Co.<span class="icon-slot"></span></div>
      <div class="contact-row">Wrenport, GA
        <svg viewBox="0 0 24 24" aria-hidden="true"><path d="M12 2a7 7 0 0 0-7 7c0 5 7 13 7 13s7-8 7-13a7 7 0 0 0-7-7zm0 9.5A2.5 2.5 0 1 1 12 6.5a2.5 2.5 0 0 1 0 5z" fill="var(--navy)"/></svg>
      </div>
      <div class="contact-row">555.318.6027
        <svg viewBox="0 0 24 24" aria-hidden="true"><path d="M6.6 10.8a15 15 0 0 0 6.6 6.6l2.2-2.2a1 1 0 0 1 1-.25 11.4 11.4 0 0 0 3.6.57 1 1 0 0 1 1 1V20a1 1 0 0 1-1 1A17 17 0 0 1 3 4a1 1 0 0 1 1-1h3.5a1 1 0 0 1 1 1c0 1.250.2 2.450.57 3.57a1 1 0 0 1-.25 1z" fill="var(--navy)"/></svg>
      </div>
      <div class="contact-row">dalbymarineco.example
        <svg viewBox="0 0 24 24" aria-hidden="true"><circle cx="12" cy="12" r="9" fill="none" stroke="var(--navy)" stroke-width="2"/><path d="M3 12h18M12 3c3 3 3 15 0 18M12 3c-3 3-3 15 0 18" fill="none" stroke="var(--navy)" stroke-width="1.6"/></svg>
      </div>
    </div>
  </section>

  <section class="card card-back" aria-label="Card back">
    <p class="brand-name">Dalby Marine Co.</p>
  </section>
</main>
</body>
</html>
```